Reputable business cards for Diplom Kauffrau, Privat und Geschäftslich

The business cards should be reputable, valuable and elegant in order to be able to use them for business. The design should also include a sophistication that is conspicuous. This could be a picture, an ornament, a sublime print or a kind of logo of the initials of my name "MD". The font should be clear and legible.
Target Market(s)
Business contacts, friends and acquaintances
Contact Information for Business Card
Diplom-Kauffrau Mirela Donat
Lindenhofweg 7 50931 Kerpen
Mobil +49 171 804 29 57
e-mail mirela.donat@postwerk.de
Colors
Designer to choose colors to be used in the design.
Requirements
Must have
- Clear and easy to read font My name in larger font than the other information Visual conspicuity / specificity
Nice to have
- Different colors
Should not have
- Ornate font, playful

```html
<!DOCTYPE html>
<html lang="de">
<head>
<meta charset="utf-8">
<title>Mirela Donat – Visitenkarten</title>
<link href="https://fonts.googleapis.com/css2?family=Montserrat:wght@700&family=Questrial&display=swap" rel="stylesheet">
<style>
  :root{
    --stage:#1f1f21;
    --card-deep:#0d1236;
    --card-light:#1a2352;
    --ink:#ffffff;
    --accent:#3cc3ec;
    --rule:#c9d3e6;
  }
  *{box-sizing:border-box;margin:0;padding:0}
  html,body{width:1200px;height:1200px;overflow:hidden;background:var(--stage)}
  .sheet{width:1200px;height:1200px;display:flex;flex-direction:column;align-items:center;justify-content:center;gap:60px}
  .card{width:860px;height:506px;position:relative;
    background:linear-gradient(135deg,var(--card-deep) 0%,var(--card-light) 100%);
    box-shadow:0 14px 30px rgba(0,0,0,.55)}
  .monogram{display:flex;align-items:center;gap:18px;color:var(--ink);
    font-family:"Montserrat",sans-serif;font-weight:700;letter-spacing:2px;line-height:1}
  .monogram__dot{border-radius:50%;background:var(--ink);flex:none}
  .name{font-family:"Questrial",sans-serif;color:var(--ink);text-transform:uppercase;letter-spacing:2px;white-space:nowrap}
  .name__first{font-family:"Montserrat",sans-serif;font-weight:700}
  .role{font-family:"Questrial",sans-serif;color:var(--accent);text-transform:uppercase;letter-spacing:2px}

  /* front */
  .card--front{display:flex;flex-direction:column;align-items:center;justify-content:center}
  .card--front .monogram{font-size:96px;margin-bottom:30px}
  .card--front .monogram__dot{width:26px;height:26px}
  .card--front .name{font-size:38px}
  .card--front .role{font-size:26px;margin-top:4px}

  /* back */
  .card--back{display:flex;align-items:center;padding-left:110px}
  .card--back .monogram{font-size:110px;width:290px}
  .card--back .monogram__dot{width:30px;height:30px}
  .divider{width:2px;height:190px;background:var(--rule);margin:0 44px 0 20px}
  .card--back .name{font-size:42px}
  .card--back .role{font-size:28px;margin-top:2px}
  .contact{list-style:none;margin-top:18px;font-family:"Questrial",sans-serif;color:var(--ink);font-size:22px}
  .contact li{display:flex;align-items:center;gap:14px;height:34px;white-space:nowrap}
  .contact svg{width:22px;height:22px;flex:none;fill:none;stroke:var(--accent);stroke-width:2}
</style>
</head>
<body>
<main class="sheet">
  <section class="card card--front">
    <div class="monogram"><span class="monogram__dot"></span>MD</div>
    <h1 class="name"><span class="name__first">Mirela</span> Donat</h1>
    <p class="role">Diplom-Kauffrau</p>
  </section>

  <section class="card card--back">
    <div class="monogram"><span class="monogram__dot"></span>MD</div>
    <span class="divider"></span>
    <div class="details">
      <h2 class="name"><span class="name__first">Mirela</span> Donat</h2>
      <p class="role">Diplom-Kauffrau</p>
      <ul class="contact">
        <li><svg viewBox="0 0 24 24"><rect x="6" y="2" width="12" height="20" rx="2"/><line x1="9" y1="18" x2="15" y2="18"/></svg>+49 171 804 29 57</li>
        <li><svg viewBox="0 0 24 24"><rect x="2" y="5" width="20" height="14"/><polyline points="2,5 12,13 22,5"/></svg>mirela.donat@postwerk.de</li>
        <li><svg viewBox="0 0 24 24"><path d="M12 22s-7-7-7-12a7 7 0 0 1 14 0c0 5-7 12-7 12z"/><circle cx="12" cy="10" r="2.5"/></svg>Lindenhofweg 7 50931 Kerpen</li>
      </ul>
    </div>
  </section>
</main>
</body>
</html>
```